Lone Cedar Haulers Billboard Design

I am needing a billboard design for my rolloff dumpster rental company. I would like to use white, black, and green colors. I also need the number 555-204-3816 to be clearly visible. I would like a modern design, but bold from the highway. It has an LED backlighting system for visibility. White would be the desired base color.
20 yard, 25 yard, 30 yard, 40 yard sizes
LOCALLY OWNED AND OPERATED
SAME DAY SERVICE

Target Market(s)

Construction Companies

Industry/Entity Type

Equipment Rental

Font styles to use
Sans Serif

Colors
59FF00
82FF00
B8FF75
E3FFCB
F4FFEA

Requirements
Must have
• Listed in Description

```html
<!DOCTYPE html>
<html lang="en">
<head>
<meta charset="utf-8">
<title>Lone Cedar Haulers Billboard</title>
<link rel="stylesheet" href="https://fonts.googleapis.com/css2?family=Archivo+Black&family=Fira+Sans:wght@500;600;700;800&family=Montserrat:wght@500;600;700&display=swap">
<style>
  :root {
    --green: #8dc63f;
    --charcoal: #58595b;
    --ink: #3d3e40;
    --white: #ffffff;
    --backdrop-light: #f4f4f5;
    --backdrop-dark: #d9dadc;
  }
  * { margin: 0; padding: 0; box-sizing: border-box; }
  html, body { width: 800px; height: 1200px; overflow: hidden; }
  body {
    background: radial-gradient(ellipse at center, var(--backdrop-light) 0%, var(--backdrop-dark) 100%);
    position: relative;
  }
  .billboard {
    position: absolute;
    left: 30px;
    top: 478px;
    width: 880px;
    height: 290px;
    transform: scale(0.8409);
    transform-origin: top left;
    filter: drop-shadow(4px 6px 6px rgba(0,0,0,0.35));
  }
  .billboard-shapes { position: absolute; inset: 0; }
  .brand-seal {
    position: absolute;
    left: 36px; top: 30px;
    width: 134px; height: 134px;
    border-radius: 50%;
    background: var(--white);
    border: 9px solid var(--charcoal);
    display: flex; align-items: center; justify-content: center;
    text-align: center;
    font: 700 17px/1.15 "Montserrat", sans-serif;
    color: var(--green);
  }
  .service-perks {
    position: absolute;
    left: 8px; top: 172px;
    width: 130px;
    font: 800 12px/1.3 "Fira Sans", sans-serif;
    letter-spacing: 0.5px;
    color: var(--white);
  }
  .company-name {
    position: absolute;
    left: 230px; width: 560px; top: 12px;
    text-align: center;
    font: 700 64px/1 "Montserrat", sans-serif;
    letter-spacing: -1px;
    color: var(--green);
  }
  .company-subline {
    position: absolute;
    left: 258px; width: 492px; top: 76px;
    display: flex; align-items: center; gap: 16px;
    font: 500 31px/1 "Montserrat", sans-serif;
    color: var(--ink);
  }
  .company-subline::before, .company-subline::after {
    content: ""; flex: 1; height: 2px; background: var(--ink);
  }
  .tagline {
    position: absolute;
    left: 214px; width: 600px; top: 113px;
    text-align: center;
    font: 700 26px/1 "Fira Sans", sans-serif;
    letter-spacing: 2px;
    color: var(--ink);
  }
  .phone-number {
    position: absolute;
    left: 262px; width: 560px; top: 152px;
    text-align: center;
    font: 400 60px/1 "Archivo Black", sans-serif;
    letter-spacing: 1px;
    color: var(--white);
  }
  .call-prompt {
    position: absolute;
    left: 240px; width: 580px; top: 216px;
    text-align: center;
    font: 600 29px/1 "Fira Sans", sans-serif;
    letter-spacing: 1.5px;
    color: var(--green);
  }
  .service-area {
    position: absolute;
    left: 240px; width: 580px; top: 257px;
    text-align: center;
    font: 600 20px/1 "Fira Sans", sans-serif;
    letter-spacing: 1.6px;
    color: var(--ink);
  }
  .local-badge {
    position: absolute;
    left: 0; top: 239px;
    width: 164px; height: 43px;
    background: var(--white);
    border-radius: 0 22px 22px 0;
    padding: 7px 0 0 14px;
    font: 600 13px/1.15 "Fira Sans", sans-serif;
    letter-spacing: 0.8px;
    color: var(--ink);
  }
</style>
</head>
<body>
  <div class="billboard">
    <svg class="billboard-shapes" viewBox="0 0 880 290" width="880" height="290" aria-hidden="true">
      <rect x="0" y="0" width="880" height="290" fill="var(--charcoal)"/>
      <rect x="0" y="8" width="870" height="274" fill="var(--white)"/>
      <path d="M0 0 H65 C80 70 120 150 175 205 L263 290 H0 Z" fill="var(--green)"/>
      <path d="M65 0 H95 C110 65 140 120 185 157 L185 212 C120 160 82 80 65 0 Z" fill="var(--charcoal)"/>
      <path d="M185 157 H800 A27.5 27.5 0 0 1 800 212 H185 Z" fill="var(--charcoal)"/>
      <path d="M175 205 L200 212 L240 252 L220 252 Z" fill="var(--white)"/>
      <rect x="232" y="250" width="636" height="2.5" fill="var(--charcoal)"/>
      <circle cx="216" cy="184" r="33" fill="var(--green)"/>
      <circle cx="216" cy="184" r="25" fill="var(--white)"/>
      <path d="M205 170 c3-2 6-1 7 2 l3 7 c1 2 0 4-2 5 l-3 2 c2 5 6 9 11 11 l2-3 c1-2 3-3 5-2 l7 3 c3 1 4 4 2 7 l-3 4 c-3 3-9 3-16-1 c-8-5-14-12-17-20 c-2-6-1-11 1-13 z" fill="var(--charcoal)"/>
      <path d="M222 170 a14 14 0 0 1 11 11 M222 164 a20 20 0 0 1 17 17" stroke="var(--charcoal)" stroke-width="2.5" fill="none" stroke-linecap="round"/>
    </svg>

    <div class="brand-seal">LONE<br>CEDAR<br>HAULERS</div>
    <div class="service-perks">20 · 25 · 30 · 40 YARD<br>SAME DAY SERVICE</div>

    <div class="company-name">LONE CEDAR</div>
    <div class="company-subline">HAULERS</div>
    <div class="tagline">THE CONSTRUCTION DEBRIS SOLUTION</div>
    <div class="phone-number">555-204-3816</div>
    <div class="call-prompt">GIVE US A CALL FOR SCHEDULING</div>
    <div class="service-area">BAYTOWN - MONT BELVIEU - CHAMBERS COUNTY</div>
    <div class="local-badge">LOCALLY OWNED<br>AND OPERATED</div>
  </div>
</body>
</html>
```